Pomar Veloz - Working hours register App needs interface design

Pomar Veloz, a 1 million users Brazilian website focused on general calculations needs an interface to an App for registering the working hours of a housemaid, a nanny, a housekeeper or other domestic workers.
The final users should be mainly housewifes.
The wireframe of the pages is in the Tirvel_layout.xls file attached.
Logo is also available in the wireframe.
The interface should be optimized for Android on Nimbus QX with a 5'' screen.
Target Market(s)
Females, educated, from 30 to 50 y.o.
Industry/Entity Type
Android

```html
<!DOCTYPE html>
<html lang="pt-BR">
<head>
<meta charset="utf-8">
<title>Pomar Veloz – Equipe</title>
<link href="https://fonts.googleapis.com/css2?family=Roboto:wght@400;500;700&display=swap" rel="stylesheet">
<style>
  :root {
    --stage: #1c1c1c;
    --status-bar: #050505;
    --status-icon: #33b5e5;
    --status-text: #e6e6e6;
    --brand-red: #e10a0a;
    --brand-red-deep: #b80000;
    --brand-red-edge: #8f0000;
    --on-brand: #ffffff;
    --row-light: #ffffff;
    --row-muted: #e6e6e6;
    --divider: #b9b9b9;
    --name-ink: #111111;
    --role-ink: #444444;
    --avatar-ring: #a9a9a9;
    --key-ink: #3d3d3d;
  }
  * { box-sizing: border-box; margin: 0; padding: 0; }
  html, body {
    width: 1200px; height: 1149px; overflow: hidden;
    background: var(--stage);
    font-family: "Roboto", Arial, sans-serif;
  }
  .showcase {
    position: relative; width: 1200px; height: 1149px;
    display: flex; justify-content: center; align-items: center; gap: 80px;
  }
  .screen {
    width: 480px; height: 838px; overflow: hidden;
    display: flex; flex-direction: column;
    box-shadow: 0 20px 60px rgba(0,0,0,.6);
  }
  .status-bar {
    height: 40px; background: var(--status-bar);
    display: flex; justify-content: flex-end; align-items: center; gap: 6px;
    padding-right: 10px;
    color: var(--status-text); font-size: 18px;
  }
  .status-bar svg { display: block; }
  .app-header {
    height: 75px; position: relative;
    background: linear-gradient(to bottom, var(--brand-red) 0%, var(--brand-red-deep) 100%);
    border-bottom: 2px solid var(--brand-red-edge);
    display: flex; align-items: center; justify-content: center;
  }
  .brand { display: flex; align-items: center; gap: 12px; }
  .brand-mark { width: 40px; height: 40px; background: var(--on-brand); border-radius: 6px; }
  .brand-name { color: var(--on-brand); font-weight: 700; font-size: 34px; letter-spacing: .2px; }
  .edit-button {
    position: absolute; right: 14px; top: 9px;
    width: 56px; height: 56px; border-radius: 6px;
    background: linear-gradient(to bottom, #f01818, #c20000);
    border: 1px solid #ff5a5a;
    box-shadow: 0 0 0 1px var(--brand-red-edge);
    display: flex; align-items: center; justify-content: center;
  }
  .staff-list { list-style: none; flex: 1; display: flex; flex-direction: column; }
  .staff-row {
    flex: 1; display: flex; align-items: center;
    padding: 0 16px 0 10px;
    border-bottom: 1px solid var(--divider);
  }
  .staff-row:last-child { border-bottom: none; }
  .screen--light .staff-list { background: var(--row-light); }
  .screen--muted .staff-list { background: var(--row-muted); }
  .avatar {
    width: 82px; height: 82px; border-radius: 50%; flex: none;
    border: 5px solid var(--avatar-ring);
  }
  .staff-info { margin-left: 10px; flex: 1; line-height: 1.1; }
  .staff-name { font-size: 28px; font-weight: 500; color: var(--name-ink); }
  .staff-role { font-size: 19px; color: var(--role-ink); margin-top: 2px; }
  .keypad-icon { width: 50px; height: 28px; flex: none; }
  .tone-dark { background: radial-gradient(circle at 45% 40%, #5b6d78, #1a2228); }
  .tone-mono { background: radial-gradient(circle at 50% 45%, #e8e8e8, #2a2a2a); }
  .tone-warm { background: radial-gradient(circle at 45% 45%, #f4d8c0, #9cc3c9); }
  .tone-olive { background: radial-gradient(circle at 50% 45%, #d9a987, #7d6e2e); }
  .tone-rose { background: radial-gradient(circle at 50% 40%, #f1d3a3, #b06f80); }
  .tone-grey { background: radial-gradient(circle at 50% 45%, #d0d0d0, #3a3a3a); }
  .tone-night { background: radial-gradient(circle at 55% 40%, #8a8a8a, #111111); }
</style>
</head>
<body>
<svg width="0" height="0" style="position:absolute">
  <symbol id="keypad" viewBox="0 0 50 28">
    <g fill="var(--key-ink)">
      <rect x="0" y="0" width="50" height="5" rx="1"/>
      <rect x="2" y="7" width="46" height="5" rx="1"/>
      <rect x="0" y="14" width="50" height="5" rx="1"/>
      <rect x="12" y="22" width="26" height="5" rx="1"/>
    </g>
    <g fill="#ffffff" opacity=".55">
      <rect x="6" y="0" width="1.5" height="19"/><rect x="12.5" y="0" width="1.5" height="19"/>
      <rect x="19" y="0" width="1.5" height="19"/><rect x="25.5" y="0" width="1.5" height="19"/>
      <rect x="32" y="0" width="1.5" height="19"/><rect x="38.5" y="0" width="1.5" height="19"/>
      <rect x="45" y="0" width="1.5" height="19"/>
    </g>
  </symbol>
  <symbol id="pencil" viewBox="0 0 32 32">
    <path d="M22 4 L28 10 L12 26 L5 28 L6 20 Z" fill="#ffffff"/>
    <path d="M20 7 L25 12" stroke="#c20000" stroke-width="2"/>
    <path d="M7 21 L11 25" stroke="#c20000" stroke-width="1.5"/>
  </symbol>
  <symbol id="status-icons" viewBox="0 0 92 24">
    <g fill="var(--status-icon)">
      <path d="M2 8 Q14 -2 26 8 L23 11 Q14 4 5 11 Z"/>
      <path d="M7 13 Q14 7 21 13 L18 16 Q14 12 10 16 Z"/>
      <circle cx="14" cy="20" r="3"/>
      <rect x="32" y="16" width="3" height="6"/><rect x="37" y="12" width="3" height="10"/>
      <rect x="42" y="8" width="3" height="14"/><rect x="47" y="3" width="3" height="19"/>
      <rect x="60" y="1" width="5" height="3"/><rect x="57" y="3" width="11" height="20" rx="1"/>
    </g>
  </symbol>
</svg>

<main class="showcase">
  <section class="screen screen--light">
    <div class="status-bar">
      <svg width="92" height="24"><use href="#status-icons"/></svg>
      <span class="clock">12:00</span>
    </div>
    <header class="app-header">
      <div class="brand"><span class="brand-mark"></span><span class="brand-name">Pomar Veloz</span></div>
      <div class="edit-button"><svg width="32" height="32"><use href="#pencil"/></svg></div>
    </header>
    <ul class="staff-list">
      <li class="staff-row"><div class="avatar tone-dark" role="img" aria-label="Profile photo of R. Calderwin"></div><div class="staff-info"><p class="staff-name">R. Calderwin</p><p class="staff-role">CEO/Founder</p></div><svg class="keypad-icon"><use href="#keypad"/></svg></li>
      <li class="staff-row"><div class="avatar tone-mono" role="img" aria-label="Profile photo of Nina T"></div><div class="staff-info"><p class="staff-name">Nina T</p><p class="staff-role">Account Manager</p></div><svg class="keypad-icon"><use href="#keypad"/></svg></li>
      <li class="staff-row"><div class="avatar tone-warm" role="img" aria-label="Profile photo of Lena Marquez"></div><div class="staff-info"><p class="staff-name">Lena Marquez</p><p class="staff-role">Marketing Specialist</p></div><svg class="keypad-icon"><use href="#keypad"/></svg></li>
      <li class="staff-row"><div class="avatar tone-olive" role="img" aria-label="Profile photo of Paul K"></div><div class="staff-info"><p class="staff-name">Paul K</p><p class="staff-role">Sr Animator</p></div><svg class="keypad-icon"><use href="#keypad"/></svg></li>
      <li class="staff-row"><div class="avatar tone-rose" role="img" aria-label="Profile photo of Hazel Moreton"></div><div class="staff-info"><p class="staff-name">Hazel Moreton</p><p class="staff-role">Sr Illustrator Artist</p></div><svg class="keypad-icon"><use href="#keypad"/></svg></li>
      <li class="staff-row"><div class="avatar tone-grey" role="img" aria-label="Profile photo of Oscar Brandt"></div><div class="staff-info"><p class="staff-name">Oscar Brandt</p><p class="staff-role">UI/UX Designer</p></div><svg class="keypad-icon"><use href="#keypad"/></svg></li>
      <li class="staff-row"><div class="avatar tone-night" role="img" aria-label="Profile photo of Tobin Hale"></div><div class="staff-info"><p class="staff-name">Tobin Hale</p><p class="staff-role">Android Developer</p></div><svg class="keypad-icon"><use href="#keypad"/></svg></li>
    </ul>
  </section>

  <section class="screen screen--muted">
    <div class="status-bar">
      <svg width="92" height="24"><use href="#status-icons"/></svg>
      <span class="clock">12:00</span>
    </div>
    <header class="app-header">
      <div class="brand"><span class="brand-mark"></span><span class="brand-name">Pomar Veloz</span></div>
      <div class="edit-button"><svg width="32" height="32"><use href="#pencil"/></svg></div>
    </header>
    <ul class="staff-list">
      <li class="staff-row"><div class="avatar tone-dark" role="img" aria-label="Profile photo of R. Calderwin"></div><div class="staff-info"><p class="staff-name">R. Calderwin</p><p class="staff-role">CEO/Founder</p></div><svg class="keypad-icon"><use href="#keypad"/></svg></li>
      <li class="staff-row"><div class="avatar tone-mono" role="img" aria-label="Profile photo of Nina T"></div><div class="staff-info"><p class="staff-name">Nina T</p><p class="staff-role">Account Manager</p></div><svg class="keypad-icon"><use href="#keypad"/></svg></li>
      <li class="staff-row"><div class="avatar tone-warm" role="img" aria-label="Profile photo of Lena Marquez"></div><div class="staff-info"><p class="staff-name">Lena Marquez</p><p class="staff-role">Marketing Specialist</p></div><svg class="keypad-icon"><use href="#keypad"/></svg></li>
      <li class="staff-row"><div class="avatar tone-olive" role="img" aria-label="Profile photo of Paul K"></div><div class="staff-info"><p class="staff-name">Paul K</p><p class="staff-role">Sr Animator</p></div><svg class="keypad-icon"><use href="#keypad"/></svg></li>
      <li class="staff-row"><div class="avatar tone-rose" role="img" aria-label="Profile photo of Hazel Moreton"></div><div class="staff-info"><p class="staff-name">Hazel Moreton</p><p class="staff-role">Sr Illustrator Artist</p></div><svg class="keypad-icon"><use href="#keypad"/></svg></li>
      <li class="staff-row"><div class="avatar tone-grey" role="img" aria-label="Profile photo of Oscar Brandt"></div><div class="staff-info"><p class="staff-name">Oscar Brandt</p><p class="staff-role">UI/UX Designer</p></div><svg class="keypad-icon"><use href="#keypad"/></svg></li>
      <li class="staff-row"><div class="avatar tone-night" role="img" aria-label="Profile photo of Tobin Hale"></div><div class="staff-info"><p class="staff-name">Tobin Hale</p><p class="staff-role">Android Developer</p></div><svg class="keypad-icon"><use href="#keypad"/></svg></li>
    </ul>
  </section>
</main>
</body>
</html>
```